Holvery Real Estate Management Consulting

To design a high end company profile that inspires confidence in high net worth individuals and similar clients. The profile to include real estate images, preferably real images. The firm is a Zambian firm and has its target to be comparable to Tesk & Company, Parlowe & Company, Wilder Osten, Lun dorv pelsin wilder osten, TLAV Real estate company as such.

Target Market(s)

Real estate clients such as high net worth individuals, private and public companies, government and international agencies, banks and insurance companies, trusts and pension funds and individual investors. the sub target market group being developers, planners, financiers, market analysts, designers, economists, engineers, architects, construction managers, quantity surveyors and public officials and others

Colors

Designer to choose colors to be used in the design.

Requirements
Must have
• Company logo

```html
<!DOCTYPE html>
<html lang="en">
<head>
<meta charset="utf-8">
<title>Holvery Real Estate Management Consulting – Company Profile Spread</title>
<link href="https://fonts.googleapis.com/css2?family=Cinzel:wght@400;600&family=Open+Sans:wght@400;600;700&display=swap" rel="stylesheet">
<style>
:root{
  --backdrop:#e4e4e6;
  --navy:#34467f;
  --navy-deep:#2c3d75;
  --lavender:#b8c1de;
  --heading:#5664a6;
  --text:#6f6f73;
  --text-soft:#8a8a8e;
  --table-head:#7f8dc0;
  --row-a:#9d9d9f;
  --row-b:#b2b2b4;
  --row-text:#f0f0f2;
  --folio:#6d6d70;
}
*{margin:0;padding:0;box-sizing:border-box}
html,body{width:1200px;height:900px;overflow:hidden;background:var(--backdrop)}
body{font-family:"Open Sans",sans-serif;color:var(--text)}
.spread{position:absolute;left:40px;top:47px;width:1120px;height:806px;display:flex;box-shadow:0 12px 30px rgba(0,0,0,.18)}
.page{position:relative;width:560px;height:806px;overflow:hidden}
.page--left{background:linear-gradient(90deg,#d4d4d6 0%,#e4e4e6 50%,#f4f4f5 92%,#dcdcde 100%)}
.page--right{background:linear-gradient(90deg,#e9e9ea 0%,#d0d0d2 45%,#bdbdbf 100%)}
.masthead{height:128px;display:flex;align-items:center;justify-content:space-between;padding:0 31px}
.page--left .masthead{background:linear-gradient(90deg,#a6b1d4 0%,#b9c2df 45%,#7d8cbe 78%,var(--navy-deep) 100%)}
.page--right .masthead{background:linear-gradient(90deg,var(--navy-deep) 0%,#4a5b97 40%,var(--navy) 100%)}
.brand{display:flex;align-items:center;gap:7px;font-family:"Open Sans",sans-serif;font-weight:700;font-size:17px;letter-spacing:2px;color:#eef0f7}
.brand__mark{width:10px;height:10px;background:#eef0f7}
.masthead__title{font-family:"Cinzel",serif;font-size:18px;letter-spacing:1px;color:#f4f5fa;margin-top:10px}
.section-title{font-weight:600;font-size:12.5px;color:var(--heading);text-transform:uppercase;letter-spacing:.3px}
.sub-title{font-weight:600;font-size:12.5px;color:var(--heading)}
p,li{font-size:8.7px;line-height:1.2;color:var(--text)}
p+p{margin-top:9px}
.intro{position:absolute;left:31px;top:167px;width:498px}
.intro p{margin-top:8px}
.core-table{position:absolute;left:31px;top:234px;width:305px}
.core-table__row{display:grid;grid-template-columns:106px 1fr;padding:6px 15px 8px}
.core-table__row--head{background:var(--table-head);padding:6px 15px}
.core-table__row--head span{font-size:8.7px;font-weight:600;color:#fff}
.core-table__row:nth-child(2){background:var(--row-a);padding-bottom:8px}
.core-table__row:nth-child(3){background:var(--row-b)}
.core-table__row:nth-child(4){background:var(--row-a)}
.core-table__label{font-size:8.7px;font-weight:600;color:var(--row-text)}
.core-table__scope{list-style:none;padding-top:7px}
.core-table__scope li{color:#e4e4e7;line-height:1.22}
.solutions{position:absolute;left:367px;top:239px;width:172px}
.solutions h3{margin-bottom:9px}
.address{position:absolute;left:31px;top:545px;width:300px}
.address h4{font-size:8.7px;font-weight:700;color:#5a5a5e;margin-bottom:12px}
.address p{color:var(--text)}
.folio{position:absolute;bottom:0;width:31px;height:31px;background:var(--folio);color:#f2f2f2;font-size:12px;display:flex;align-items:center;justify-content:center}
.page--left .folio{left:0}
.page--right .folio{right:0}
.services-intro{position:absolute;left:31px;top:165px;width:500px}
.services-intro .section-title{margin-bottom:9px}
.advisory{margin-top:17px}
.advisory h4{font-size:8.7px;font-weight:600;color:#606064;margin-bottom:12px}
.col{position:absolute;top:407px}
.col--left{left:31px;width:242px}
.col--right{left:293px;width:238px}
.col h3{margin-bottom:11px}
.col ul{list-style:none;margin-top:5px}
.col ul li::before{content:"•";margin-right:5px}
.col .block{margin-top:12px}
.spine{position:absolute;left:548px;top:0;width:24px;height:806px;background:linear-gradient(90deg,rgba(0,0,0,0) 0%,rgba(0,0,0,.12) 50%,rgba(0,0,0,0) 100%);pointer-events:none}
</style>
</head>
<body>
<div class="spread">
  <section class="page page--left">
    <header class="masthead">
      <div class="brand"><span class="brand__mark"></span>HOLVERY</div>
      <div class="masthead__title">INSPIRE VALUE</div>
    </header>

    <div class="intro">
      <h2 class="section-title">Who we are</h2>
      <p>Holvery | Management Consulting is one of Zambia`s leading professional real estate services firms with an outstanding reputation and has its cornerstone the excellence of its people. Since its inception, the business has continued successfully with a national client base, a number of which have retained our services.</p>
    </div>

    <div class="core-table">
      <div class="core-table__row core-table__row--head"><span>Core Services</span><span>Scope</span></div>
      <div class="core-table__row">
        <span class="core-table__label">Consulting</span>
        <ul class="core-table__scope">
          <li>Advisory Services</li>
          <li>Acquisition, Leasing &amp; Disposal Advise</li>
          <li>Business Plans</li>
          <li>Feasibility studies</li>
          <li>Highest and Best Use Studies</li>
          <li>Market research/analysis</li>
          <li>Planning and development</li>
          <li>Property Condition Assessments</li>
        </ul>
      </div>
      <div class="core-table__row">
        <span class="core-table__label">Valuations</span>
        <ul class="core-table__scope">
          <li>Agriculture Valuations</li>
          <li>Asset Valuations</li>
          <li>Commercial Valuations</li>
          <li>Leisure/Hotels/Lodges</li>
          <li>Industrial Valuations</li>
          <li>Special purpose Valuations</li>
          <li>Mines Valuations</li>
          <li>Residential Valuations</li>
          <li>Plant, Machinery &amp; Equipment</li>
        </ul>
      </div>
      <div class="core-table__row">
        <span class="core-table__label">Firm's Reference</span>
        <ul class="core-table__scope">
          <li>The Valuers Registration Council</li>
          <li>Registration Board</li>
          <li>P.O Box 40012</li>
          <li>Lusaka</li>
        </ul>
      </div>
    </div>

    <div class="solutions">
      <h3 class="sub-title">Our Solutions</h3>
      <p>As a preferred property firm we continually monitor property value levels and will provide you with an update on market rents, trends and the position of your property in the marketplace.</p>
      <p>We continue to roll out our real estate services for you our clients to benefit from the power of our massive experience and database.</p>
      <p>Our system allows you to save on unnecessary research costs and time of doing new research in the marketplace and all due diligence is done when identifying the interests, benefits and rights being researched.</p>
      <p>We assure our clients and prospective clients that our work is independent, objective and compliant with nationally recognized Laws of the Republic of Zambia.</p>
    </div>

    <div class="address">
      <h4>Our address is as follows:</h4>
      <p>Messrs. Holvery | Management Consulting<br>
      Unit 3, Plot NO. 2210<br>
      Meridian Road<br>
      Kafue, Lusaka Province– Zambia<br>
      Mobile:&nbsp;&nbsp; +260 900 400 112/ 0900 215730<br>
      E-mail: info@holveryproperty.com</p>
    </div>

    <div class="folio">2</div>
  </section>

  <section class="page page--right">
    <header class="masthead">
      <div class="masthead__title">SMART MOVE</div>
      <div class="brand"><span class="brand__mark"></span>HOLVERY</div>
    </header>

    <div class="services-intro">
      <h2 class="section-title">Services and business lines</h2>
      <p>Holvery Mgt Consulting serves our clients through four main business lines with services for all property types and asset classes.</p>
      <div class="advisory">
        <h4>Advisory Services</h4>
        <p>Our advisory services help communities find strategic practical solutions for the most challenging issues facing today`s urban, suburban and rural areas.</p>
        <p>We provide expert, independent, timing, candid, and biased input from national real estate, land use, design and planning experts. We help communities gain fresh insight and come to innovative solutions for complex land use and real estate development challenges.</p>
        <p>Our work aims to work with local governments, private developers, community development corporations and many other organizations to address the most challenging real estate and land use issues facing the communities today.</p>
        <p>Holvery| Mgt consulting works with industry leaders including developers, planners, financiers, market analysts, designers, economists, engineers, architects, construction managers, quantity surveyors and public officials to provide practical and objective advise that is not available from any other source.</p>
      </div>
    </div>

    <div class="col col--left">
      <h3 class="sub-title">Property Consultancy</h3>
      <p>As the property market has matured, we have provided consultancy advice to clients in the areas of relocation, market overview, research, planning and development, and property investment.</p>
      <p>Our consultancy services include:</p>
      <ul>
        <li>Acquisition, Leasing and Disposal advice</li>
        <li>Facilities Management advisory</li>
        <li>Highest and Best Use Studies</li>
        <li>Landlord and Tenant representation</li>
        <li>Market research/analysis</li>
        <li>Planning and development</li>
        <li>Property management advisory</li>
      </ul>
      <div class="block">
        <h3 class="sub-title">Urban Planning and Development</h3>
        <p>Urban planning and development involves the design and organization of urban space and activities.</p>
        <p>We undertake due diligence and feasibility studies for landowners, developers and investors as regards the processes and considerations involved in development.</p>
        <p>We also undertake market analysis and demand forecasting; development feasibility and risk assessment; and make recommendations on how to implement an effective development project, including marketing and attracting potential development partners.</p>
      </div>
    </div>

    <div class="col col--right">
      <h3 class="sub-title">Valuation Services</h3>
      <p>Holvery Mgt provides comprehensive valuation, advisory and consulting services for real estate owners, investors and lenders, combining our specialized expertise and premier technologies to deliver industry-leading valuation reports and analysis.</p>
      <p>We focus on the valuation of various land and building assets, including agricultural, commercial, industrial, residential, retail, development sites and specialized properties.</p>
      <p>We act for private and public companies, government and international agencies, banks and insurance companies, trusts and pension funds and individual investors.</p>
      <p>Uses of Valuation Services:</p>
      <ul>
        <li>Auction reserves valuations</li>
        <li>Collateral Valuations</li>
        <li>Financial Reporting</li>
        <li>Insurance Valuations</li>
        <li>Legal/ Judgment purposes</li>
        <li>Property Transfer Tax</li>
        <li>Purchase and/or Sale among others</li>
        <li>Rental Valuations</li>
      </ul>
    </div>

    <div class="folio">3</div>
  </section>
  <div class="spine"></div>
</div>
</body>
</html>
```